Private Learning Centre in Singapore needs a flyer design

We need a flyer design for our upcoming education fair and also able to use it for day to day purpose. The aim is to attract parents, students to enrol for classes by offering them free trial class/assessment. 2 sided flyer with the front page as the logo only and details on the other page. We would like to see a final design in blue, white and it should be curious and attractive enough not to allow customers to throw it away once they received it.

Education

```html
<!DOCTYPE html>
<html lang="en">
<head>
<meta charset="utf-8">
<title>Bright Path Academy – Free Trial Classes</title>
<link rel="stylesheet" href="https://fonts.googleapis.com/css2?family=Caladea&family=Cinzel+Decorative:wght@700&family=Tinos:wght@700&display=swap">
<style>
  :root {
    --paper: #ffffff;
    --frame-light: #9db8dc;
    --frame-dark: #5b86c0;
    --headline: #5a5ae0;
    --ink: #1b1b1b;
    --brand: #3a52a0;
    --link: #1a1ae6;
    --box-line: #dcdcdc;
  }
  html, body {
    margin: 0;
    padding: 0;
    overflow: hidden;
    background: var(--paper);
  }
  .flyer {
    position: relative;
    width: 927px;
    height: 1200px;
    background: var(--paper);
    overflow: hidden;
  }
  .frame {
    position: absolute;
    inset: 0;
  }
  .ribbon {
    position: absolute;
    margin: 0;
    font-family: "Cinzel Decorative", serif;
    font-weight: 700;
    font-size: 40px;
    line-height: 44px;
    letter-spacing: 1px;
    text-align: center;
    color: var(--paper);
    -webkit-text-stroke: 1.5px var(--headline);
    white-space: nowrap;
  }
  .ribbon--left {
    left: 60px;
    top: 110px;
    transform: rotate(-26deg);
  }
  .ribbon--right {
    left: 585px;
    top: 125px;
    transform: rotate(27deg);
  }
  .intro {
    position: absolute;
    left: 85px;
    top: 282px;
    width: 770px;
    margin: 0;
    font-family: "Caladea", serif;
    font-size: 33px;
    line-height: 62.5px;
    color: var(--ink);
  }
  .brand-box {
    position: absolute;
    left: 97px;
    top: 862px;
    width: 292px;
    height: 286px;
    border: 1px solid var(--box-line);
    box-sizing: border-box;
    display: flex;
    align-items: center;
    justify-content: center;
    gap: 12px;
  }
  .brand-name {
    font-family: "Caladea", serif;
    font-size: 28px;
    line-height: 34px;
    color: var(--brand);
    text-align: center;
  }
  .contact {
    position: absolute;
    left: 398px;
    top: 866px;
    margin: 0;
    font-family: "Tinos", serif;
    font-weight: 700;
    font-size: 23px;
    line-height: 40px;
    color: var(--ink);
    font-style: normal;
  }
  .contact a {
    color: var(--link);
    text-decoration: underline;
  }
  .social {
    position: absolute;
    left: 452px;
    top: 1050px;
    display: flex;
    align-items: center;
    gap: 10px;
    font-family: "Tinos", serif;
    font-weight: 700;
    font-size: 23px;
    color: var(--brand);
  }
  .social-square {
    width: 22px;
    height: 22px;
    background: var(--brand);
  }
</style>
</head>
<body>
<main class="flyer">
  <svg class="frame" width="927" height="1200" viewBox="0 0 927 1200" aria-hidden="true">
    <rect x="45" y="45" width="839" height="1108" fill="none" stroke="var(--frame-light)" stroke-width="6"/>
    <rect x="64" y="66" width="801" height="1064" fill="none" stroke="var(--frame-light)" stroke-width="6"/>
    <g fill="var(--paper)" stroke="var(--frame-dark)" stroke-width="2">
      <rect x="27" y="26" width="64" height="64"/>
      <rect x="36" y="35" width="46" height="46"/>
      <rect x="835" y="26" width="64" height="64"/>
      <rect x="844" y="35" width="46" height="46"/>
      <rect x="27" y="1103" width="64" height="64"/>
      <rect x="36" y="1112" width="46" height="46"/>
      <rect x="835" y="1103" width="64" height="64"/>
      <rect x="844" y="1112" width="46" height="46"/>
    </g>
  </svg>

  <p class="ribbon ribbon--left">FREE TRIAL<br>CLASSES</p>
  <p class="ribbon ribbon--right">FREE TRIAL<br>CLASSES</p>

  <p class="intro">Bright Path Academy is where you can develop academic and life skills. Our teachers are the heartbeat of the business. They inspire and nurture students, helping them surpass their expectations.&nbsp; We cover English, Mathematics and Science from Primary and Secondary Levels.</p>

  <div class="brand-box">
    <span class="brand-name">Bright Path<br>Academy</span>
  </div>

  <address class="contact">
    Bright Path Academy<br>
    118 Seaview Lane S428190<br>
    6512 0847<br>
    <a href="mailto:hello@brightpathacademy.com">hello@brightpathacademy.com</a>
  </address>

  <div class="social">
    <span class="social-square"></span>
    <span>Chatterbook</span>
  </div>
</main>
</body>
</html>
```